Business Card cabinets and cabinets components making company.

the card should be formal and interesting at the same time. The main colors will be black and white.

Font styles to use
Sans Serif

Colors

Designer to choose only greyscale colors for use in the design.

Requirements
Must have
• At least must have the followings:
office phone
cell phone
address
position
name
email
web

```html
<!DOCTYPE html>
<html lang="en">
<head>
<meta charset="utf-8">
<title>Oakline Cabinetry – Business Card</title>
<link rel="stylesheet" href="https://fonts.googleapis.com/css2?family=Roboto+Condensed:wght@400;700&family=Roboto:wght@400;500&display=swap">
<style>
  :root {
    --page: #d9d9d9;
    --card: #ffffff;
    --ink: #1f1f1f;
    --band: #202020;
    --band-text: #f2f2f2;
    --muted: #bdbdbd;
  }
  * { box-sizing: border-box; margin: 0; padding: 0; }
  html, body { width: 1200px; height: 800px; overflow: hidden; }
  body {
    background: var(--page);
    font-family: "Roboto", Arial, sans-serif;
    color: var(--ink);
  }
  .canvas {
    position: relative;
    width: 1200px;
    height: 800px;
    display: flex;
    align-items: center;
    justify-content: center;
    gap: 40px;
  }
  .card {
    position: relative;
    width: 540px;
    height: 309px;
    background: var(--card);
    border-radius: 18px;
    overflow: hidden;
    box-shadow: 0 10px 30px rgba(0,0,0,0.18);
  }
  .brand-name {
    font-family: "Roboto Condensed", Arial, sans-serif;
    font-weight: 700;
    color: var(--ink);
    letter-spacing: 0.5px;
    white-space: nowrap;
  }

  /* Front */
  .card-front {
    display: flex;
    flex-direction: column;
    align-items: center;
    justify-content: center;
  }
  .card-front .brand-name { font-size: 46px; }
  .card-front .website {
    margin-top: 26px;
    font-size: 12px;
    letter-spacing: 5px;
    color: var(--ink);
  }

  /* Back */
  .card-back .brand-area {
    height: 128px;
    display: flex;
    align-items: center;
    justify-content: center;
  }
  .card-back .brand-name { font-size: 40px; }
  .contact-band {
    height: 136px;
    background: var(--band);
    color: var(--band-text);
    display: flex;
    align-items: center;
    justify-content: center;
    gap: 22px;
  }
  .person { text-align: right; }
  .person-name {
    font-family: "Roboto Condensed", Arial, sans-serif;
    font-weight: 700;
    font-size: 20px;
    letter-spacing: 0.5px;
  }
  .person-role {
    font-size: 13px;
    color: var(--muted);
    margin-top: 2px;
  }
  .divider {
    width: 1px;
    height: 70px;
    background: var(--band-text);
  }
  .contact-list { list-style: none; font-size: 13.5px; }
  .contact-list li {
    display: flex;
    align-items: center;
    gap: 9px;
    line-height: 22px;
  }
  .contact-list svg { width: 12px; height: 12px; fill: var(--band-text); flex: none; }
  .address-strip {
    height: 45px;
    display: flex;
    align-items: center;
    justify-content: center;
    font-size: 13px;
    letter-spacing: 1px;
  }
</style>
</head>
<body>
<main class="canvas">

  <section class="card card-front" aria-label="Card front">
    <div class="brand-name">Oakline Cabinetry</div>
    <div class="website">www.oaklinecabinetry.com</div>
  </section>

  <section class="card card-back" aria-label="Card back">
    <div class="brand-area">
      <div class="brand-name">Oakline Cabinetry</div>
    </div>
    <div class="contact-band">
      <div class="person">
        <div class="person-name">DANIEL REEVES</div>
        <div class="person-role">Manager</div>
      </div>
      <div class="divider"></div>
      <ul class="contact-list">
        <li>
          <svg viewBox="0 0 24 24" aria-hidden="true"><path d="M6.6 10.8a15.2 15.2 0 0 0 6.6 6.6l2.2-2.2c.3-.3.7-.4 1-.2 1.1.4 2.3.6 3.6.6.6 0 1 .4 1 1V20c0 .6-.4 1-1 1A17 17 0 0 1 3 4c0-.6.4-1 1-1h3.5c.6 0 1 .4 1 1 0 1.3.2 2.5.6 3.6.1.3 0 .7-.2 1z"/></svg>
          555-210-4417
        </li>
        <li>
          <svg viewBox="0 0 24 24" aria-hidden="true"><path d="M7 1h10a2 2 0 0 1 2 2v18a2 2 0 0 1-2 2H7a2 2 0 0 1-2-2V3a2 2 0 0 1 2-2zm0 3v14h10V4zm5 15.5a1.2 1.2 0 1 0 0 2.4 1.2 1.2 0 0 0 0-2.4z"/></svg>
          555-210-4418
        </li>
        <li>
          <svg viewBox="0 0 24 24" aria-hidden="true"><path d="M2 5h20v14H2zm2 2v.5l8 5 8-5V7zm0 2.9V17h16V9.9l-8 5z"/></svg>
          hello@oaklinecabinetry.com
        </li>
      </ul>
    </div>
    <div class="address-strip">PO Box 48, 17 Mill Road, Ashford</div>
  </section>

</main>
</body>
</html>
```